Dental marketing ad poster

I recently opened a new dental practice about 2 months ago and would like to have an ad designed for an A-frame poster to place outside our office. The goal of this ad is to attract and appeal to potential patients so they feel encouraged to come into the practice.
I’m leaving the creative direction up to you—I’d like to see what you can come up with. The ad can be funny or serious, but it should be eye-catching and patient-focused. Please highlight that we provide crowns, implants and teeth whitening.
My theme color is green but I’ll accept any color
Let me see your ideas!
Dentistry

```html
<!DOCTYPE html>
<html lang="en">
<head>
<meta charset="UTF-8">
<title>Willowmere Dentistry – Tips for Good Dental Care</title>
<link rel="stylesheet" href="https://fonts.googleapis.com/css2?family=Fredoka:wght@500;600&family=Nunito:wght@300;400&family=Yellowtail&display=block">
<style>
  :root {
    --blue-deep: #0f35c2;
    --blue-mid: #1557e0;
    --blue-bright: #1a95f2;
    --lime: #a4dd1f;
    --white: #ffffff;
    --card-line: rgba(255,255,255,0.9);
    --art-light: #eef8d6;
    --art-lime: rgba(164,221,31,0.55);
    --page: #eef0f3;
  }
  * { box-sizing: border-box; margin: 0; padding: 0; }
  html, body { width: 842px; height: 1200px; overflow: hidden; background: var(--page); }
  .poster {
    position: relative;
    width: 842px; height: 1200px;
    background: radial-gradient(ellipse 70% 45% at 55% 42%, var(--blue-bright) 0%, var(--blue-mid) 55%, var(--blue-deep) 100%);
    color: var(--white);
    font-family: "Nunito", sans-serif;
    overflow: hidden;
  }
  .brand {
    position: absolute; top: 58px; left: 0; width: 100%;
    text-align: center;
    font-family: "Fredoka", sans-serif; font-weight: 600; color: var(--white);
  }
  .brand-name { display: block; font-size: 64px; line-height: 1; }
  .brand-sub { display: block; font-size: 30px; letter-spacing: 12px; margin-top: 10px; }

  .tips-heading { position: absolute; top: 205px; left: 0; width: 100%; text-align: center; font-family: "Fredoka", sans-serif; font-weight: 600; }
  .tips-heading .lead { display: block; font-size: 30px; letter-spacing: 1px; }
  .tips-heading .highlight {
    display: inline-block; margin-top: 6px; padding: 2px 16px 4px;
    background: var(--lime); border-radius: 6px;
    font-size: 50px; line-height: 1.1; color: var(--white);
  }

  .tip-card {
    position: absolute; width: 272px; height: 168px;
    border: 2px solid var(--card-line); border-radius: 22px;
    padding: 26px 18px;
  }
  .tip-card h3 { font-family: "Fredoka", sans-serif; font-weight: 500; color: var(--lime); font-size: 19px; line-height: 1.2; margin-bottom: 8px; }
  .tip-card p { font-size: 13px; font-weight: 400; line-height: 1.38; }
  .tip-card.left { left: 148px; text-align: right; padding-left: 40px; }
  .tip-card.right { left: 428px; padding-right: 40px; }
  .row-1 { top: 340px; }
  .row-2 { top: 525px; }

  .illustration {
    position: absolute; width: 150px; height: 160px;
    background: radial-gradient(closest-side, var(--white) 0%, var(--art-light) 40%, var(--art-lime) 70%, rgba(164,221,31,0) 100%);
  }
  .illus-brush { left: 18px; top: 345px; }
  .illus-floss { left: 676px; top: 335px; }
  .illus-checkup { left: 18px; top: 530px; }
  .illus-diet { left: 676px; top: 525px; }

  .slogan {
    position: absolute; top: 735px; left: 0; width: 100%; text-align: center;
    font-family: "Yellowtail", "Brush Script MT", cursive; font-size: 70px; line-height: 1;
  }

  .services-title {
    position: absolute; top: 860px; left: 0; width: 100%;
    display: flex; justify-content: center; align-items: center; gap: 14px;
    font-family: "Fredoka", sans-serif; font-weight: 600; font-size: 24px;
  }
  .services-title .rule { width: 120px; height: 2px; background: linear-gradient(90deg, rgba(255,255,255,0), var(--white)); }
  .services-title .rule.end { background: linear-gradient(90deg, var(--white), rgba(255,255,255,0)); }
  .services-title .accent { color: var(--lime); }

  .services { position: absolute; top: 905px; left: 50px; width: 742px; display: flex; justify-content: space-between; }
  .service { width: 210px; text-align: center; }
  .service-ring { position: relative; width: 200px; height: 200px; margin: 0 auto; }
  .service-ring svg { position: absolute; inset: 0; }
  .service-art {
    position: absolute; left: 32px; top: 32px; width: 136px; height: 136px; border-radius: 50%;
    background: radial-gradient(closest-side, #ffffff 0%, #f3dcd2 55%, #e9b3a4 100%);
  }
  .service-art.whitening { background: radial-gradient(closest-side, #ffffff 0%, #e8eef8 50%, #f2cf55 100%); }
  .service-label { margin-top: 14px; font-family: "Fredoka", sans-serif; font-weight: 600; font-size: 26px; line-height: 1.15; }
  .service-label .lime { color: var(--lime); }
</style>
</head>
<body>
<main class="poster">
  <header class="brand">
    <span class="brand-name">Willowmere</span>
    <span class="brand-sub">DENTISTRY</span>
  </header>

  <h2 class="tips-heading">
    <span class="lead">TIPS FOR GOOD</span>
    <span class="highlight">DENTAL CARE</span>
  </h2>

  <section class="tip-card left row-1">
    <h3>REGULAR BRUSHING</h3>
    <p>Brush your teeth at least twice a day, preferably in the morning and before bedtime, using a toothbrush with soft bristles.</p>
  </section>
  <div class="illustration illus-brush" role="img" aria-label="Illustration of tiny people brushing a giant tooth"></div>

  <section class="tip-card right row-1">
    <h3>USE DENTAL FLOSS</h3>
    <p>Use dental floss daily to clean between your teeth and remove plaque that your toothbrush may not reach.</p>
  </section>
  <div class="illustration illus-floss" role="img" aria-label="Illustration of dentists examining a large tooth beside a chart"></div>

  <section class="tip-card left row-2">
    <h3>REGULAR DENTAL<br>CHECKUPS</h3>
    <p>Schedule regular dental checkups, at least twice a year, for preventive checkups and professional cleanings.</p>
  </section>
  <div class="illustration illus-checkup" role="img" aria-label="Illustration of a patient in a dental chair with a dentist"></div>

  <section class="tip-card right row-2">
    <h3>HEALTHY DIET<br>FOR TEETH</h3>
    <p>Consume a balanced diet that includes foods rich in calcium and avoid excessive sugar.</p>
  </section>
  <div class="illustration illus-diet" role="img" aria-label="Illustration of a dentist showing a tooth chart to a parent and child"></div>

  <p class="slogan">Get the Perfect Smile !</p>

  <h2 class="services-title">
    <span class="rule"></span>
    <span>OUR <span class="accent">SERVICES</span></span>
    <span class="rule end"></span>
  </h2>

  <div class="services">
    <article class="service">
      <div class="service-ring">
        <svg viewBox="0 0 200 200" aria-hidden="true">
          <defs><linearGradient id="ring-a" x1="0" y1="0" x2="1" y2="1"><stop offset="0" stop-color="#a4dd1f"/><stop offset="1" stop-color="#ffffff"/></linearGradient></defs>
          <circle cx="100" cy="100" r="96" fill="none" stroke="url(#ring-a)" stroke-width="3"/>
          <circle cx="100" cy="100" r="84" fill="none" stroke="rgba(255,255,255,0.7)" stroke-width="2"/>
        </svg>
        <div class="service-art" role="img" aria-label="Illustration of a dental crown over a tooth in gum"></div>
      </div>
      <h3 class="service-label"><span class="lime">TEETH</span><br>CROWNS</h3>
    </article>
    <article class="service">
      <div class="service-ring">
        <svg viewBox="0 0 200 200" aria-hidden="true">
          <circle cx="100" cy="100" r="96" fill="none" stroke="url(#ring-a)" stroke-width="3"/>
          <circle cx="100" cy="100" r="84" fill="none" stroke="rgba(255,255,255,0.7)" stroke-width="2"/>
        </svg>
        <div class="service-art" role="img" aria-label="Illustration of a dental implant between two teeth"></div>
      </div>
      <h3 class="service-label">TEETH<br><span class="lime">IMPLANTS</span></h3>
    </article>
    <article class="service">
      <div class="service-ring">
        <svg viewBox="0 0 200 200" aria-hidden="true">
          <circle cx="100" cy="100" r="96" fill="none" stroke="url(#ring-a)" stroke-width="3"/>
          <circle cx="100" cy="100" r="84" fill="none" stroke="rgba(255,255,255,0.7)" stroke-width="2"/>
        </svg>
        <div class="service-art whitening" role="img" aria-label="Illustration of a tooth being cleaned white with foam"></div>
      </div>
      <h3 class="service-label"><span class="lime">TEETH</span><br>WHITENING</h3>
    </article>
  </div>
</main>
</body>
</html>
```